Sidewalk Sign For Laundry Service

I'd like to make a sign that offers *free* laundry service for the next customers that bring in their laundry. There needs to be some immediacy in the design. The idea is to put out this sign when we are idle in the laundry and want to use the time to attract new customers. So somehow we need to communicate that the offer is for right now and will likely be gone in an hour or two. Attached are photos of the sign holder in place to give a feel for the location and environment. Obviously I'm looking for a much better design that the one currently in use.

Requirements:
* 23.25" x 35.5" - the full width will be visible but the top and bottom 0.5" will be hidden by the sign holder. It will be printed on coroplast.
* Must include a large arrow to show where the service is offered. We're off the main street so the arrow helps a lot. See the attached pictures of the sign being replaced.
* Needs to be visible to cars as they drive by.
* For the final product I'll need three versions. One with an arrow pointing to the right, one with an arrow pointing to the left, and one to go in the store window with no arrow.

Background on the service: We sort, wash, dry, and fold the laundry for customers and then neatly put it in a nice laundry bag that makes returning very convenient. Their laundry comes out fresh, clean, smelling great, and without the hassle of doing it themselves. We have a great return rate. Most customers that try out the service become long term customers.

Attached are two pictures of the sign holder with our current "Laundry Wash & Fold" sign. Also, our logo which would be nice to include to help with branding.

```html
<!DOCTYPE html>
<html lang="en">
<head>
<meta charset="utf-8">
<title>Fresh Fold Laundry – FREE Today Only</title>
<link rel="stylesheet" href="https://fonts.googleapis.com/css2?family=Archivo+Black&family=Patrick+Hand&family=Arimo:wght@400&display=swap">
<style>
  :root {
    --navy: #2a479d;
    --sky: #8bbbe6;
    --mid: #5f98d3;
    --pale: #b9d6f0;
    --orange: #f26522;
    --white: #ffffff;
  }
  html, body {
    margin: 0;
    padding: 0;
    width: 785px;
    height: 1200px;
    overflow: hidden;
    background: var(--white);
  }
  .sign {
    display: block;
    width: 785px;
    height: 1200px;
  }
  .brand-name {
    font-family: "Archivo Black", sans-serif;
    font-size: 50px;
    fill: var(--navy);
  }
  .brand-mark { fill: var(--navy); }
  .offer-shadow {
    font-family: "Archivo Black", sans-serif;
    font-size: 430px;
    fill: var(--navy);
  }
  .offer-word {
    font-family: "Archivo Black", sans-serif;
    font-size: 430px;
    fill: var(--sky);
    stroke: var(--navy);
    stroke-width: 6px;
    paint-order: stroke;
  }
  .headline {
    font-family: "Archivo Black", sans-serif;
    font-size: 138px;
    fill: var(--navy);
  }
  .services {
    font-family: "Patrick Hand", cursive;
    font-size: 132px;
    fill: var(--navy);
  }
  .wave-pale { fill: var(--pale); }
  .wave-mid { fill: var(--mid); }
  .wave-deep { fill: var(--navy); }
  .arrow {
    fill: var(--orange);
    stroke: var(--navy);
    stroke-width: 9px;
    stroke-linejoin: miter;
  }
  .fine-print {
    font-family: "Arimo", sans-serif;
    font-size: 26px;
    fill: var(--white);
  }
</style>
</head>
<body>
<svg class="sign" viewBox="0 0 785 1200" xmlns="http://www.w3.org/2000/svg">
  <defs>
    <linearGradient id="bubble-tone" x1="0" y1="0" x2="0" y2="1">
      <stop offset="0" stop-color="#a9cdee"/>
      <stop offset="1" stop-color="#3f67b5"/>
    </linearGradient>
  </defs>

  <!-- brand -->
  <g class="brand">
    <rect class="brand-mark" x="172" y="42" width="120" height="120" rx="10"/>
    <text class="brand-name" x="312" y="96">Fresh Fold</text>
    <text class="brand-name" x="312" y="156">Laundry</text>
  </g>

  <!-- offer -->
  <g class="offer">
    <text class="offer-shadow" x="26" y="537" textLength="712" lengthAdjust="spacingAndGlyphs">FREE</text>
    <text class="offer-word" x="42" y="545" textLength="712" lengthAdjust="spacingAndGlyphs">FREE</text>
    <text class="headline" x="213" y="680" textLength="534" lengthAdjust="spacingAndGlyphs">Today Only!!</text>
    <text class="services" x="42" y="812" textLength="700" lengthAdjust="spacingAndGlyphs">sort•wash•dry</text>
  </g>

  <!-- waves -->
  <g class="waves">
    <path class="wave-pale" d="M0 900 C140 840 300 850 430 905 S690 1000 785 930 V1200 H0 Z"/>
    <path class="wave-mid" d="M0 950 C160 900 320 930 460 985 S700 1050 785 990 V1200 H0 Z"/>
    <path class="wave-deep" d="M0 1025 C170 985 340 1010 500 1060 S720 1085 785 1030 V1200 H0 Z"/>
  </g>

  <g role="img" aria-label="Soap bubbles rising from the wave">
    <rect x="30" y="885" width="140" height="250" rx="60" fill="url(#bubble-tone)" opacity="0.45"/>
  </g>

  <!-- direction arrow -->
  <path class="arrow" d="M462 910 H590 V862 L748 962 L590 1062 V1014 H462 Z"/>

  <text class="fine-print" x="156" y="1170" textLength="474" lengthAdjust="spacingAndGlyphs">Offer valid to new customers ONLY</text>
</svg>
</body>
</html>
```